Design bcard for Velmora Advising and Coaching LLC

I need a logo inspired by the term Velmora. I'd like to have type of work I do on the back side, i.e. provide A and C on DEIJ, SDOH,...... Front of card--business name, contact information, and possibly a tag line.

Target Market(s)

NGOs, human service agencies, education, healthcare, public health.

Contact Information for Business Card

Name of business, email address, phone number, logo--on front. Services on the back

Font styles to use
Sans Serif

Requirements
Must have
• Contact information, creative logo, services

```html
<!DOCTYPE html>
<html lang="en">
<head>
<meta charset="utf-8">
<title>Velmora Advising and Coaching LLC — Business Card</title>
<link href="https://fonts.googleapis.com/css2?family=Lato:wght@400;700;900&display=swap" rel="stylesheet">
<style>
  :root {
    --brand-blue: #1b7bbd;
    --brand-purple: #a0479c;
    --ink: #444444;
    --paper: #ffffff;
    --page: #ffffff;
    --faint-pink: #efe2ef;
  }
  * { box-sizing: border-box; margin: 0; padding: 0; }
  html, body {
    width: 1070px; height: 1200px; overflow: hidden;
    background: var(--page);
    font-family: "Lato", Arial, sans-serif;
  }
  .card {
    position: absolute; left: 210px; width: 653px; height: 374px;
    border-radius: 20px; overflow: hidden;
    box-shadow: 0 1px 3px rgba(0,0,0,.35);
  }
  .card--front { top: 193px; background: var(--paper); border: 1px solid #e2e2e2; }
  .card--back { top: 679px; background: var(--brand-blue); }

  .wordmark {
    position: absolute; display: flex; align-items: center; gap: 9px;
    font-weight: 900; line-height: 1; letter-spacing: -1px; white-space: nowrap;
  }
  .wordmark__dot { border-radius: 50%; flex: none; }
  .front-mark { left: 44px; top: 48px; font-size: 62px; color: var(--brand-blue); }
  .front-mark .wordmark__dot { width: 13px; height: 13px; background: var(--brand-purple); }
  .front-sub {
    position: absolute; left: 57px; top: 116px;
    font-size: 12px; letter-spacing: 3.3px; color: var(--brand-purple); white-space: nowrap;
  }

  .contact-list { position: absolute; left: 58px; top: 146px; list-style: none; }
  .contact-list li {
    display: flex; align-items: center; height: 24.9px;
    font-size: 15.5px; letter-spacing: 1px; color: var(--ink); white-space: nowrap;
  }
  .contact-list svg { width: 13px; height: 13px; margin-right: 11px; fill: var(--brand-purple); }

  .accent-circle {
    position: absolute; left: 552px; top: 102px; width: 78px; height: 78px;
    border-radius: 50%; background: var(--faint-pink);
  }
  .person { position: absolute; right: 45px; top: 173px; text-align: right; white-space: nowrap; }
  .person__name { font-size: 30px; font-weight: 700; color: var(--brand-blue); letter-spacing: 1px; line-height: 1; }
  .person__role { font-size: 18.5px; color: var(--brand-purple); letter-spacing: 1px; margin-top: 6px; }

  .wave { position: absolute; left: 0; top: 0; width: 100%; height: 100%; }
  .tagline {
    position: absolute; left: 0; right: 0; top: 347px; text-align: center;
    color: #fff; font-size: 15px; letter-spacing: 1px;
  }

  .back-mark {
    left: 0; right: 0; justify-content: center; top: 128px;
    font-size: 86px; color: #fff;
  }
  .back-mark .wordmark__dot { width: 18px; height: 18px; background: #fff; }
  .back-sub {
    position: absolute; left: 0; right: 0; top: 216px; text-align: center;
    color: #fff; font-size: 19.5px; letter-spacing: 4.6px; white-space: nowrap;
  }
  .services {
    position: absolute; left: 0; right: 0; top: 303px; text-align: center;
    color: #fff; font-size: 16.5px; line-height: 21px;
  }
</style>
</head>
<body>

<section class="card card--front" aria-label="Card front">
  <div class="accent-circle"></div>

  <div class="wordmark front-mark"><span class="wordmark__dot"></span>VELMORA</div>
  <div class="front-sub">ADVISING AND COACHING LLC</div>

  <ul class="contact-list">
    <li><svg viewBox="0 0 16 16"><path d="M3 1l3 3-2 2c1 2 3 4 5 5l2-2 3 3-2 3C6 15 1 10 1 3z"/></svg>(555) 201-4730</li>
    <li><svg viewBox="0 0 16 16"><path d="M4 0h8a1 1 0 0 1 1 1v14a1 1 0 0 1-1 1H4a1 1 0 0 1-1-1V1a1 1 0 0 1 1-1zm1 2v10h6V2z"/></svg>(555) 201-4731</li>
    <li><svg viewBox="0 0 16 16"><path d="M4 1h8v4H4zM1 6h14v6h-3v3H4v-3H1zm4 4v3h6v-3z"/></svg>(555) 201-4732</li>
    <li><svg viewBox="0 0 16 16"><path d="M1 3h14v10H1zm1 1.5V12h12V4.5L8 9z"/></svg>info@yourwebsite.com</li>
    <li><svg viewBox="0 0 16 16"><path d="M8 1a7 7 0 1 0 0 14A7 7 0 0 0 8 1zm0 2a5 5 0 0 1 4.6 3H10L8 4 6 6l1 3-2 2-1.5-.5A5 5 0 0 1 8 3z"/></svg>yourwebsite.com</li>
  </ul>

  <div class="person">
    <div class="person__name">DANIEL REYES</div>
    <div class="person__role">Founder &amp; CEO</div>
  </div>

  <svg class="wave" viewBox="0 0 646 369" preserveAspectRatio="none" aria-hidden="true">
    <path d="M0 257 Q 300 352 585 293 Q 300 342 0 270 Z" fill="var(--brand-purple)"/>
    <path d="M0 279 Q 330 368 646 276 L646 369 L0 369 Z" fill="var(--brand-blue)"/>
  </svg>
  <div class="tagline">YOUR TAGLINE GOES HERE</div>
</section>

<section class="card card--back" aria-label="Card back">
  <div class="wordmark back-mark"><span class="wordmark__dot"></span>VELMORA</div>
  <div class="back-sub">ADVISING AND COACHING LLC</div>
  <p class="services">
    Health Care &amp; Quality | Neihgborhood &amp; Built Environment | Ecnomic Stability<br>
    Social and Community Context | Education Access and Quality
  </p>
</section>

</body>
</html>
```